Kivo Commercial Cleaning is lookong for a new business card design.

A fresh new design that's professional and stylish. We need a serious upgrade to our business cards. I have included pictures of our existing ones. Our clients include professional individuals and business owners. We woupdblike something professional and upbeat. Please have fun and see what you come uo with.

Target Market(s)

Property managers, business owners, facility managers and other similar professionals

Industry/Entity Type

Janitorial

Contact Information for Business Card

Name, cell, office number, email, web address

Font styles to use
Sans Serif

Colors

Designer to choose colors to be used in the design.

Requirements
Must have
• please use the green color in our logo
Nice to have
• Bar code
Should not have
• Address

```html
<!DOCTYPE html>
<html lang="en">
<head>
<meta charset="utf-8">
<title>Kivo Commercial Cleaning – Business Card</title>
<link href="https://fonts.googleapis.com/css2?family=Arimo:wght@400;700&display=swap" rel="stylesheet">
<style>
  :root {
    --green: #39b55a;
    --blue: #2f5fa6;
    --ink: #4a4a4a;
    --paper: #ffffff;
    --backdrop: #e4e4e4;
  }
  * { margin: 0; padding: 0; box-sizing: border-box; }
  html, body { width: 1200px; height: 1200px; overflow: hidden; }
  body {
    position: relative;
    background: var(--backdrop);
    font-family: "Arimo", Arial, sans-serif;
  }
  .card {
    position: absolute;
    left: 262px;
    width: 686px;
    height: 392px;
    border-radius: 22px;
    overflow: hidden;
  }
  .card--front { top: 165px; background: var(--paper); }
  .card--back { top: 653px; background: var(--green); }

  .brand {
    position: absolute;
    font-weight: 700;
    text-align: center;
    line-height: 1;
  }
  .card--front .brand {
    left: 80px; width: 280px; top: 140px;
    color: var(--green);
  }
  .card--back .brand {
    left: 0; width: 686px; top: 110px;
    color: var(--paper);
  }
  .brand__name { display: block; letter-spacing: -2px; }
  .card--front .brand__name { font-size: 96px; }
  .card--back .brand__name { font-size: 150px; }
  .brand__line { display: block; }
  .card--front .brand__line { font-size: 20px; margin-top: 6px; }
  .card--back .brand__line { font-size: 30px; margin-top: 10px; }

  .divider {
    position: absolute;
    left: 358px; top: 140px;
    width: 1px; height: 135px;
    background: #cfcfcf;
  }
  .contact { position: absolute; left: 381px; top: 148px; }
  .contact__name {
    font-size: 27px; font-weight: 700; color: var(--green);
    margin-bottom: 22px;
  }
  .contact__list { list-style: none; }
  .contact__item {
    display: flex; align-items: center;
    font-size: 17px; color: var(--ink);
    height: 21px;
  }
  .contact__item svg { width: 14px; height: 14px; margin-right: 10px; flex: none; }

  .band-line {
    position: absolute; left: 0; right: 0; top: 374px;
    height: 2px; background: var(--blue);
  }
  .band {
    position: absolute; left: 0; right: 0; top: 378px; bottom: 0;
    background: var(--green);
  }
</style>
</head>
<body>
  <section class="card card--front" aria-label="Business card front">
    <div class="brand">
      <span class="brand__name">Kivo</span>
      <span class="brand__line">Commercial Cleaning</span>
    </div>
    <div class="divider"></div>
    <div class="contact">
      <p class="contact__name">Maren Okafor</p>
      <ul class="contact__list">
        <li class="contact__item">
          <svg viewBox="0 0 24 24" aria-hidden="true"><path fill="#2f5fa6" d="M6.6 10.8a15.1 15.1 0 0 0 6.6 6.6l2.2-2.2c.3-.3.7-.4 1-.2 1.1.4 2.3.6 3.6.6.6 0 1 .4 1 1V20c0 .6-.4 1-1 1A17 17 0 0 1 3 4c0-.6.4-1 1-1h3.5c.6 0 1 .4 1 1 0 1.3.2 2.5.6 3.6.1.3 0 .7-.2 1z"/></svg>
          (555) 014-2287
        </li>
        <li class="contact__item">
          <svg viewBox="0 0 24 24" aria-hidden="true"><rect x="2" y="5" width="20" height="14" fill="#2f5fa6"/><path d="M3 6l9 7 9-7" fill="none" stroke="#fff" stroke-width="1.6"/></svg>
          maren@kivocleaning.com
        </li>
        <li class="contact__item">
          <svg viewBox="0 0 24 24" aria-hidden="true"><circle cx="12" cy="12" r="10" fill="#2f5fa6"/><path d="M12 2c3 3 3 17 0 20M2 12h20M4.5 7h15M4.5 17h15" fill="none" stroke="#fff" stroke-width="1.3"/></svg>
          www.kivocleaning.com
        </li>
      </ul>
    </div>
    <div class="band-line"></div>
    <div class="band"></div>
  </section>

  <section class="card card--back" aria-label="Business card back">
    <div class="brand">
      <span class="brand__name">Kivo</span>
      <span class="brand__line">Commercial Cleaning</span>
    </div>
  </section>
</body>
</html>
```